International Trading Company, 'KIRO' needs a Business Card

The company name is "KIRO" and it has own logo design.
I'd like to use its logo on this business card.
I need two side Business Card.
I'll look forward to your great design.
Thank you very much in advance.

Contact Information for Business Card

Company Name : Kiro Harbour Limited
Information Example
Dorian Pallister
Mobile(use icon please) : 1 (212) 555-0143
Tel(use icon please) : 1 (212) 555-0178
Email(use icon please) : dorian27@kiroharbour-mail.com
Address(use icon please) : 482 Halden Ave, New York, NY 10160, USA

```html
<!DOCTYPE html>
<html lang="en">
<head>
<meta charset="UTF-8">
<title>Kiro Harbour Limited — Business Card</title>
<link rel="stylesheet" href="https://fonts.googleapis.com/css2?family=Arimo:wght@700&family=Open+Sans:wght@400;600&display=swap">
<style>
  :root {
    --page-bg: #e9e7e4;
    --strip-black: #151515;
    --logo-panel: #ffffff;
    --info-panel: #545456;
    --logo-grey: #58585a;
    --text-light: #f2f2f2;
    --name-grey: #e4e4e4;
    --back-black: #0a0a0a;
    --pattern-tone: #141414;
    --back-mark: #8a8a8a;
  }
  * { margin: 0; padding: 0; box-sizing: border-box; }
  html, body { width: 1200px; height: 900px; overflow: hidden; }
  body { background: var(--page-bg); position: relative; font-family: "Open Sans", sans-serif; }

  .card { position: absolute; box-shadow: 0 6px 18px rgba(0,0,0,0.18); overflow: hidden; }

  .card-front { left: 148px; top: 66px; width: 589px; height: 365px; display: flex; }
  .edge-strip { width: 44px; background: var(--strip-black); }
  .logo-panel { width: 174px; background: var(--logo-panel); position: relative; }
  .logo-word {
    position: absolute; left: 50%; top: 50%;
    transform: translate(-50%, -50%) rotate(-90deg);
    font-family: "Arimo", sans-serif; font-weight: 700;
    font-size: 92px; letter-spacing: 4px; color: var(--logo-grey);
    white-space: nowrap; line-height: 1;
  }
  .info-panel { flex: 1; background: var(--info-panel); position: relative; color: var(--text-light); }
  .holder-name {
    position: absolute; left: 38px; top: 46px;
    font-family: "Arimo", sans-serif; font-weight: 700; font-size: 20px;
    letter-spacing: 0.3px; color: var(--name-grey);
  }
  .contact-list { position: absolute; left: 38px; top: 168px; list-style: none; }
  .contact-list li { display: flex; align-items: center; height: 21px; font-size: 15px; }
  .contact-list svg { width: 13px; height: 13px; margin-right: 8px; fill: var(--text-light); flex: none; }
  .address-block { position: absolute; left: 38px; top: 260px; display: flex; }
  .address-block svg { width: 13px; height: 16px; margin: 5px 8px 0 0; fill: var(--text-light); flex: none; }
  .company-name { font-weight: 600; font-size: 18px; line-height: 24px; }
  .address-line { font-size: 16px; line-height: 22px; }

  .card-back { left: 400px; top: 459px; width: 566px; height: 350px; background: var(--back-black); }
  .back-pattern { position: absolute; inset: 0; background: linear-gradient(180deg, var(--pattern-tone), var(--back-black)); }
  .back-mark {
    position: absolute; left: 410px; top: 249px;
    font-family: "Arimo", sans-serif; font-weight: 700; font-size: 15px;
    letter-spacing: 1px; color: var(--back-mark);
  }
</style>
</head>
<body>
  <section class="card card-front" aria-label="Business card front">
    <div class="edge-strip"></div>
    <div class="logo-panel"><span class="logo-word">KIRO</span></div>
    <div class="info-panel">
      <h1 class="holder-name">DORIAN PALLISTER</h1>
      <ul class="contact-list">
        <li>
          <svg viewBox="0 0 12 16" aria-hidden="true"><path d="M2 0h8a1.5 1.5 0 0 1 1.5 1.5v13A1.5 1.5 0 0 1 10 16H2A1.5 1.5 0 0 1 .5 14.5v-13A1.5 1.5 0 0 1 2 0zm0 2v10h8V2zm4 11a1 1 0 1 0 0 2 1 1 0 0 0 0-2z"/></svg>
          1 (212) 555-0178
        </li>
        <li>
          <svg viewBox="0 0 16 14" aria-hidden="true"><path d="M0 4c0-2 3-3 8-3s8 1 8 3v1.5h-4V4H4v1.5H0zm3 3h10l2 6H1zm5 1.5a2 2 0 1 0 0 4 2 2 0 0 0 0-4z"/></svg>
          1 (212) 555-0143
        </li>
        <li>
          <svg viewBox="0 0 16 12" aria-hidden="true"><path d="M0 0h16v12H0zm1.5 1.5v.4L8 6.5l6.5-4.6v-.4zm0 2.2V10.5h13V3.7L8 8.3z"/></svg>
          dorian27@kiroharbour-mail.com
        </li>
      </ul>
      <div class="address-block">
        <svg viewBox="0 0 12 16" aria-hidden="true"><path d="M6 0a6 6 0 0 1 6 6c0 4-6 10-6 10S0 10 0 6a6 6 0 0 1 6-6zm0 3.5a2.5 2.5 0 1 0 0 5 2.5 2.5 0 0 0 0-5z"/></svg>
        <div>
          <div class="company-name">Kiro Harbour Limited</div>
          <div class="address-line">482 Halden Ave, New York</div>
          <div class="address-line">NY 10160, USA</div>
        </div>
      </div>
    </div>
  </section>

  <section class="card card-back" aria-label="Business card back">
    <div class="back-pattern" role="img" aria-label="Dark tone-on-tone repeating company name pattern"></div>
    <span class="back-mark">KIRO</span>
  </section>
</body>
</html>
```